Author Needs a Book Cover for a Business Book

Title: THE AMBER HARBOR LANTERN LEDGER
Subtitle: Rivers, Orchards, and Weathervanes
Author: Belvina Throckett-Ashe, MBA, EdM, ACC, CPTD

Context: Please design a business-oriented book cover, with a minimalist, clean, and professional look.

Image to include a person (the coach either as a woman or non-specific) gender) looking into the horizon and see the three types of coaching engagement which are: group, 1:1 or virtual

Images need to be high definition for a book cover (print, digital, and audio). Back and spine design, jacket cover, audiobook cover and source files.
Format: Vector (but unsure)
AI assisted is ok, but would prefer original images
Note: I've attached a PPT with inspirational ideas but I am open to ideas.

```html
<!DOCTYPE html>
<html lang="en">
<head>
<meta charset="utf-8">
<title>The Amber Harbor Lantern Ledger – Book Cover</title>
<link rel="stylesheet" href="https://fonts.googleapis.com/css2?family=Bebas+Neue&family=Lexend:wght@500;600&display=swap">
<style>
  :root {
    --backdrop: #4d4d4d;
    --paper: #dfe6ea;
    --navy: #243e80;
    --cyan: #00b4e0;
    --photo-top: #b89170;
    --photo-mid: #6687bb;
    --photo-bottom: #4e6fa3;
  }
  html, body {
    margin: 0;
    width: 1200px;
    height: 1200px;
    overflow: hidden;
    background: var(--backdrop);
  }
  .stage {
    width: 1200px;
    height: 1200px;
    display: flex;
    align-items: center;
    justify-content: center;
  }
  .book-cover {
    width: 672px;
    height: 952px;
    display: block;
  }
  .cover-paper { fill: var(--paper); }
  .ring-fill { fill: var(--navy); }
  .inner-disc { fill: var(--paper); }
  .sweep-band { fill: none; stroke: var(--navy); }
  .author-name {
    font-family: "Lexend", sans-serif;
    font-weight: 600;
    font-size: 31px;
    fill: var(--navy);
  }
  .author-credentials {
    font-family: "Lexend", sans-serif;
    font-weight: 600;
    font-size: 18px;
    fill: var(--navy);
  }
  .title-line {
    font-family: "Bebas Neue", sans-serif;
    font-size: 133px;
  }
  .title-line--cyan { fill: var(--cyan); }
  .title-line--navy { fill: var(--navy); }
  .subtitle {
    font-family: "Bebas Neue", sans-serif;
    font-size: 36px;
    fill: var(--navy);
  }
</style>
</head>
<body>
<main class="stage">
  <svg class="book-cover" viewBox="0 0 842 1190" xmlns="http://www.w3.org/2000/svg">
    <defs>
      <clipPath id="cover-clip"><rect width="842" height="1190"/></clipPath>
      <clipPath id="ring-lower"><rect x="0" y="415" width="842" height="800"/></clipPath>
      <clipPath id="band-lower"><rect x="0" y="760" width="842" height="440"/></clipPath>
      <linearGradient id="photo-tones" x1="0" y1="0" x2="0" y2="1">
        <stop offset="0" stop-color="var(--photo-top)"/>
        <stop offset="0.4" stop-color="var(--photo-mid)"/>
        <stop offset="1" stop-color="var(--photo-bottom)"/>
      </linearGradient>
    </defs>

    <g clip-path="url(#cover-clip)">
      <rect class="cover-paper" width="842" height="1190"/>

      <!-- halo ring behind the title -->
      <circle class="ring-fill" cx="418" cy="415" r="410"/>
      <circle class="ring-fill" cx="410" cy="420" r="422" clip-path="url(#ring-lower)"/>
      <circle class="inner-disc" cx="418" cy="418" r="366"/>

      <!-- sweeping lower band -->
      <circle class="sweep-band" cx="418" cy="520" r="680" stroke-width="110" clip-path="url(#band-lower)"/>

      <!-- coach photo area -->
      <rect role="img" aria-label="Photo: a woman in a blue blouse seen from behind, hands on hips, looking toward the horizon"
            x="125" y="640" width="615" height="485" rx="28" fill="url(#photo-tones)"/>

      <!-- author -->
      <text class="author-name" x="418" y="153" text-anchor="middle">Belvina Throckett-Ashe</text>
      <text class="author-credentials" x="418" y="189" text-anchor="middle">MBA, EdM, ACC, CPTD</text>

      <!-- title -->
      <text class="title-line title-line--cyan" x="113" y="323" textLength="614" lengthAdjust="spacingAndGlyphs">THE AMBER HARBOR</text>
      <text class="title-line title-line--navy" x="113" y="442" textLength="614" lengthAdjust="spacing">LANTERN</text>
      <text class="title-line title-line--cyan" x="113" y="562" textLength="614" lengthAdjust="spacing">LEDGER</text>

      <!-- subtitle -->
      <text class="subtitle" x="167" y="615" textLength="513" lengthAdjust="spacingAndGlyphs">RIVERS, ORCHARDS, AND WEATHERVANES</text>
    </g>
  </svg>
</main>
</body>
</html>
```